K & T GbR
Zielgruppe
Planung, Beratung, Verkauf und Montage von Fenstern und Küchen
Aufgabenstellung
Mir ist wichtig, dass die Farben des Designs der Visitenkarte später auch zu einem schwarzen T-Shirt passen.

```html
<!DOCTYPE html>
<html lang="de">
<head>
<meta charset="utf-8">
<title>Kessler &amp; Thalberg GbR – Briefbogen</title>
<link href="https://fonts.googleapis.com/css2?family=Jost:wght@300;400&display=swap" rel="stylesheet">
<style>
  :root {
    --ink: #000000;
    --paper: #ffffff;
    --accent: #d7182a;
    --text: #1a1a1a;
  }
  * { margin: 0; padding: 0; box-sizing: border-box; }
  html, body {
    width: 848px; height: 1200px; overflow: hidden;
    background: var(--paper);
    font-family: "Jost", "Futura", sans-serif;
    color: var(--text);
  }
  .letterhead { position: relative; width: 848px; height: 1200px; }

  .masthead {
    position: absolute; left: 0; top: 0; width: 848px; height: 115px;
    background: var(--ink);
  }
  .company-name {
    position: absolute; left: 94px; top: 40px;
    display: flex; align-items: center; gap: 10px;
    color: var(--paper); font-weight: 400; font-size: 22px;
    line-height: 1; white-space: nowrap;
  }
  .company-mark {
    width: 10px; height: 10px; background: var(--accent); flex: none;
  }

  .return-address {
    position: absolute; left: 95px; top: 154px;
    font-size: 7.6px; font-weight: 300; white-space: nowrap; letter-spacing: -0.1px;
  }
  .return-address .street { font-weight: 400; }

  .footer {
    position: absolute; left: 0; top: 1129px; width: 848px; height: 32px;
  }
  .footer-col {
    position: absolute; top: 7px;
    font-size: 8.4px; line-height: 11px; white-space: nowrap; letter-spacing: -0.15px;
  }
  .footer-col.light { font-weight: 300; }
  .footer-divider {
    position: absolute; top: 0; width: 1.5px; height: 32px; background: var(--accent);
  }
  .divider-1 { left: 230px; }
  .divider-2 { left: 329px; }
  .divider-3 { left: 458px; }
  .col-address { left: 102px; }
  .col-phone { left: 240px; }
  .col-web { left: 342px; }
  .col-web .url { font-weight: 300; }
  .col-bank { left: 469px; }
</style>
</head>
<body>
<div class="letterhead">
  <header class="masthead">
    <div class="company-name"><span class="company-mark"></span>Kessler &amp; Thalberg GbR</div>
  </header>

  <div class="return-address">KESSLER &amp; THALBERG GBR - <span class="street">AHORNWEG 2-4 - 53179 BONN (MEHLEM)</span></div>

  <footer class="footer">
    <div class="footer-col col-address">AHORNWEG 2-4<br>53179 BONN (MEHLEM)</div>
    <div class="footer-divider divider-1"></div>
    <div class="footer-col col-phone">TEL: 0228 987654<br>MOBIL: 0171 2259083</div>
    <div class="footer-divider divider-2"></div>
    <div class="footer-col col-web">THALBERG@MAILPOST.DE<br><span class="url">www.kesslerundthalberg.de</span></div>
    <div class="footer-divider divider-3"></div>
    <div class="footer-col col-bank light">Nordbank (10020030)<br>Kontonummer: 123 45 67</div>
  </footer>
</div>
</body>
</html>
```